依頼詳細
このチラシは 2月中旬に公的な機関(駅・市役所・市の施設)を中心に設置します。本法人のウェブサイトにもアップいたします。
記載項目
社名:あおばねオンライン寺子屋(個別学習指導)
℡番号:03-5817-2240
URL:https://verdalo-kanto.jp
QRコードを作成お願いいたします。
ロゴマークは添付しております。
キャッチコピー:「いっでんそばにおっでな!」…I'll come and stay with you at any time.の鹿児島弁です。
サイズ
A4
ページ数
片面
希望イメージ
シンプル 複雑
単色 カラフル
暗い 明るい
日常 高級
遊び心 厳粛
未来的 伝統的
女性的 男性的
希望する色
赤系、青系
納品ファイル
• 高解像度JPG (.jpg)
• イラストレーター形式 (.ai)
補足説明
添付資料「パンフ原稿」pp1-2を参考にしてください。全部使用する必要はありません。
念のために…
主催団体:一般社団法人ヴェルダロ青少年グローバル交流センター
所在地:〒150-0093 東京都渋谷区桐ケ丘3-8-24-402
はロゴマーク、QRコード、URL、e-mail アドレスなどとともに記載必須です。

重要事項…インターネット環境とパソコンさえあれば受講できます。
体験授業は3月から随時。4月から本格的に授業開始。
参加ご希望者はウェブサイトよりお申し込みください。
作品ご応募を検討される皆様へ
チラシをラックに置くことも考慮し、タイトルの「青羽オンライン寺子屋(個別学習)」をチラシ上部にデザインしていただきますようお願いいたします。
■ 選んだ理由

当選された方には まだ修正していただくことがございますが 笑顔の少年のイメージが弊社の考えていたイメージにマッチしていたことです。弊社の希望する色遣いの赤・青とは異なっていましたが それを差し引いても 随所に出品者様の工夫やご提案がありました。こういう姿勢も大切かと思いました。

■ 提案者全員のお礼・コメント

短期間に甲乙つけがたい作品が14作品も結集いたしましたことを心より御礼申し上げます。いつもそうですが 1つに絞ることを心苦しく思います。お許しください。遠隔地の教育に力を入れたいという弊社の取り組みに300名を超える方の閲覧を受け さらにはご応募いただきましたことを重ねてお礼申し上げます。

```html
<!DOCTYPE html>
<html lang="ja">
<head>
<meta charset="utf-8">
<title>青羽オンライン寺子屋 受講者募集</title>
<link rel="stylesheet" href="https://fonts.googleapis.com/css2?family=M+PLUS+1p:wght@500;700;800;900&family=Noto+Sans+JP:wght@400;500;700;900&display=swap">
<style>
:root{
  --red:#e8382c;
  --red-dark:#c92a20;
  --orange:#f29600;
  --navy:#1b3a8a;
  --blue:#2a62b8;
  --sky:#e6f0fa;
  --ink:#2b2b2b;
  --grey:#8c8c8c;
  --paper:#ffffff;
}
*{margin:0;padding:0;box-sizing:border-box}
html,body{width:854px;height:1200px;overflow:hidden;background:var(--paper)}
body{font-family:"Noto Sans JP",sans-serif;color:var(--ink);position:relative}
.flyer{position:relative;width:854px;height:1200px;overflow:hidden}

/* header */
.hero{position:absolute;left:0;top:0;width:854px;height:358px;background:var(--red)}
.hero__lead{position:absolute;top:16px;width:100%;text-align:center;color:#fff;font-family:"M PLUS 1p",sans-serif;font-weight:800;font-size:21px;letter-spacing:2px}
.hero__badge{position:absolute;left:92px;top:54px;width:52px;height:52px;border-radius:8px;background:var(--orange);color:#fff;font-weight:900;font-size:15px;line-height:19px;display:flex;align-items:center;justify-content:center;text-align:center}
.hero__title{position:absolute;left:156px;top:40px;color:#fff;font-family:"M PLUS 1p",sans-serif;font-weight:900;font-size:60px;letter-spacing:1px;white-space:nowrap}
.hero__recruit{position:absolute;left:590px;top:116px;background:#fff;color:var(--red);font-weight:900;font-size:18px;padding:2px 14px;border-radius:4px;letter-spacing:3px}
.mode{position:absolute;top:150px;width:262px;height:132px;background:#fff;border-radius:10px;padding:8px}
.mode--online{left:74px}
.mode--offline{left:518px}
.mode__tag{display:inline-block;font-weight:900;font-size:14px;color:#fff;padding:1px 10px;border-radius:10px}
.mode--online .mode__tag{background:var(--red)}
.mode--offline .mode__tag{background:var(--blue)}
.mode__freq{font-size:12px;font-weight:700;margin-left:6px}
.mode__art{margin-top:6px;width:100%;height:92px;border-radius:6px}
.mode--online .mode__art{background:linear-gradient(135deg,#fde3df,#dfe9f7)}
.mode--offline .mode__art{background:linear-gradient(135deg,#e4eefb,#fbe7d3)}
.hero__plus{position:absolute;left:377px;top:148px;width:100px;height:100px}
.hero__claim{position:absolute;left:0;top:276px;width:100%;text-align:center;color:#fff;font-family:"M PLUS 1p",sans-serif;font-weight:900;font-size:30px;line-height:38px}

/* intro */
.intro{position:absolute;left:60px;top:372px;width:734px;font-size:15px;font-weight:700;line-height:26px;color:var(--navy);text-align:center}

.question{position:absolute;left:56px;top:434px;width:742px;height:84px;background:var(--sky);border-radius:10px;display:flex;align-items:center;padding:0 18px;gap:18px}
.question__head{font-family:"M PLUS 1p",sans-serif;font-weight:900;font-size:22px;line-height:28px;color:var(--navy);width:230px}
.question__bubble{flex:1;background:#fff;border:2px solid var(--blue);border-radius:10px;padding:7px 12px;font-size:12.5px;line-height:19px;color:var(--ink)}

/* points */
.points-label{position:absolute;left:18px;top:532px;width:40px;height:336px;background:var(--orange);border-radius:20px;color:#fff;font-family:"M PLUS 1p",sans-serif;font-weight:900;font-size:22px;writing-mode:vertical-rl;display:flex;align-items:center;justify-content:center;letter-spacing:4px}
.point{position:absolute;width:370px}
.point--1{left:70px;top:532px}
.point--2{left:450px;top:532px}
.point--3{left:70px;top:740px}
.point--4{left:450px;top:740px}
.point__head{display:flex;align-items:center;gap:8px;border-bottom:2px solid var(--orange);padding-bottom:4px;margin-bottom:7px}
.point__num{width:30px;height:30px;border-radius:50%;background:var(--orange);color:#fff;font-weight:900;font-size:18px;display:flex;align-items:center;justify-content:center;flex:none}
.point__title{font-family:"M PLUS 1p",sans-serif;font-weight:900;font-size:18px;color:var(--navy)}
.point__text{font-size:12.5px;line-height:19px}
.point__text em{font-style:normal;color:var(--red);font-weight:700}
.fee{margin-top:6px;border-collapse:collapse;font-size:12.5px}
.fee td{padding:2px 10px 2px 0}
.fee .price{text-align:right}
.fee .total{color:var(--red);font-weight:900;font-size:20px;padding-left:10px}

/* bottom */
.equip{position:absolute;left:56px;top:888px;width:486px;height:52px;border-radius:8px;background:#f1f1f1;display:flex;align-items:center;gap:12px;padding:0 12px}
.equip__art{width:70px;height:38px;border-radius:4px;background:linear-gradient(135deg,#cfd6df,#eef1f4)}
.equip__text{font-size:13px;font-weight:700;line-height:18px}
.equip__text strong{color:var(--red);font-size:15px}
.apply{position:absolute;left:56px;top:950px;width:486px;height:150px;background:var(--navy);border-radius:10px;color:#fff;padding:16px 20px;font-size:16px;font-weight:700;line-height:30px}
.apply span{color:#ffd54a}
.contact{position:absolute;left:558px;top:888px;width:240px;height:212px;border:2px solid var(--red);border-radius:10px;text-align:center;padding:14px 10px}
.contact__catch{display:inline-block;background:var(--red);color:#fff;font-family:"M PLUS 1p",sans-serif;font-weight:900;font-size:15px;padding:3px 12px;border-radius:14px}
.contact__sub{font-size:11px;color:var(--grey);margin-top:10px}
.brand{display:flex;align-items:center;justify-content:center;gap:6px;margin-top:6px}
.brand__mark{width:16px;height:16px;border-radius:50%;background:var(--red)}
.brand__name{font-weight:900;font-size:17px;color:var(--red)}
.contact__tel{margin-top:14px;font-weight:900;font-size:19px;color:var(--navy)}
.contact__url{margin-top:4px;font-size:13px;color:var(--navy)}

.footer{position:absolute;left:0;top:1118px;width:854px;height:82px;border-top:3px solid var(--red);display:flex;align-items:center;gap:14px;padding:0 56px}
.footer__mark{width:26px;height:26px;background:var(--navy)}
.footer__org{font-weight:900;font-size:17px;color:var(--ink)}
.footer__addr{font-size:12.5px;color:var(--grey);margin-top:3px}
</style>
</head>
<body>
<main class="flyer">
  <header class="hero">
    <p class="hero__lead">〜 東京レベルの教育を受けたいなら！ 〜</p>
    <div class="hero__badge">個別<br>学習</div>
    <h1 class="hero__title">青羽オンライン寺子屋</h1>
    <div class="hero__recruit">受講者募集</div>

    <div class="mode mode--online">
      <span class="mode__tag">オンライン</span><span class="mode__freq">週1回</span>
      <div class="mode__art" role="img" aria-label="自宅と東京をテレビ会議システムでつなぐ授業のイラスト"></div>
    </div>
    <svg class="hero__plus" viewBox="0 0 100 100" aria-hidden="true">
      <rect x="38" y="8" width="24" height="84" rx="4" fill="#fff"/>
      <rect x="8" y="38" width="84" height="24" rx="4" fill="#fff"/>
    </svg>
    <div class="mode mode--offline">
      <span class="mode__tag">オフライン</span><span class="mode__freq">月1回</span>
      <div class="mode__art" role="img" aria-label="塾での対面個別指導のイラスト"></div>
    </div>

    <p class="hero__claim">地域格差のない<br>最新教育システム！</p>
  </header>

  <p class="intro">インターネット上で、リアルタイムに東京の大学生が直接指導！<br>お一人おひとりの状況をしっかり把握し、オーダーメイドの学びで学力向上に貢献します。</p>

  <section class="question">
    <h2 class="question__head">オンライン授業で、<br>満足できる？</h2>
    <p class="question__bubble">ぜひ保護者様も一緒に体験授業を受講してみてください。ウェブカメラや手元のカメラで講師が【学習の様子】や【ノート】を見ているので、しっかりと対面授業の学びを実感できます。</p>
  </section>

  <div class="points-label">4つのポイント</div>

  <section class="point point--1">
    <div class="point__head"><span class="point__num">1</span><h3 class="point__title">リーズナブルな料金体系</h3></div>
    <p class="point__text">「オンライン寺子屋」は安心の定額制。<br>塾に通う交通費や時間も必要ありません。</p>
    <table class="fee">
      <tr><td>小学生　月4回（60分授業）</td><td></td></tr>
      <tr><td>入会金</td><td class="price">5,000円</td></tr>
      <tr><td>年会費</td><td class="price">6,000円</td></tr>
      <tr><td>月額料金</td><td class="price">→ 税込<span class="total">29,000円</span></td></tr>
    </table>
  </section>

  <section class="point point--2">
    <div class="point__head"><span class="point__num">3</span><h3 class="point__title">質の高い学習指導</h3></div>
    <p class="point__text">「オンライン寺子屋」の<em>講師は現役東京大学生</em>です。すべての講師が学習指導の研修を修了しています。<br>また、講師と保護者が定期的に面談を行い、<em>学習計画を一緒に立てる</em>ので安心です。<br>地方では身近な存在ではない東京の大学生と話すことで、学ぶ意欲や将来への視野が広がります。</p>
  </section>

  <section class="point point--3">
    <div class="point__head"><span class="point__num">2</span><h3 class="point__title">授業ごとに「指導レポート」送信</h3></div>
    <p class="point__text">授業後、講師から<em>「指導レポート」</em>をメールで送信します。授業の内容や理解度、次回までの課題をまとめ、ご家庭での学習にもお役立ていただけます。</p>
  </section>

  <section class="point point--4">
    <div class="point__head"><span class="point__num">4</span><h3 class="point__title">充実のサポート</h3></div>
    <p class="point__text">機器の接続や操作に不安がある方も、<em>専任スタッフがいつでもサポート</em>します。授業日程の変更や学習相談もお気軽にご連絡ください。</p>
  </section>

  <div class="equip">
    <div class="equip__art" role="img" aria-label="パソコンとヘッドセットとウェブカメラのイラスト"></div>
    <p class="equip__text">パソコン、ヘッドセット、webカメラ<br><strong>必要機器は無料で貸出します！</strong></p>
  </div>

  <section class="apply">
    <p>インターネット環境とパソコンさえあれば受講できます。</p>
    <p><span>体験授業は3月から随時。</span>4月から本格的に授業開始。</p>
    <p>参加ご希望者はウェブサイトより<br>お申し込みください。</p>
  </section>

  <aside class="contact">
    <p class="contact__catch">いっでんそばにおっでな！</p>
    <p class="contact__sub">個別学習指導</p>
    <div class="brand"><span class="brand__mark"></span><span class="brand__name">あおばねオンライン寺子屋</span></div>
    <p class="contact__tel">TEL. 03-5817-2240</p>
    <p class="contact__url">https://verdalo-kanto.jp</p>
  </aside>

  <footer class="footer">
    <span class="footer__mark"></span>
    <div>
      <p class="footer__org">一般社団法人ヴェルダロ青少年グローバル交流センター</p>
      <p class="footer__addr">〒150-0093 東京都渋谷区桐ケ丘3-8-24-402</p>
    </div>
  </footer>
</main>
</body>
</html>
```